Brenna Coltrane Electrical would like a flyer to advertise to businesses with our services listed. our website is brennacoltraneelectrical-example.com

Target Market(s)

Businesses and homes

Industry/Entity Type

Electrical

```html
<!DOCTYPE html>
<html lang="en">
<head>
<meta charset="utf-8">
<title>Brenna Coltrane Electrical – Flyer</title>
<link rel="stylesheet" href="https://fonts.googleapis.com/css2?family=Lora:ital,wght@1,600&family=Open+Sans:wght@400;600;700;800&family=Roboto+Condensed:wght@700;800&display=swap">
<style>
  :root{
    --ink:#1d2a36;
    --navy:#163a5c;
    --teal:#167f92;
    --green:#3aa447;
    --green-dark:#2a8a37;
    --red:#d2261d;
    --sky:#dcedf6;
    --sky-deep:#8fc3df;
    --gold:#d9b25a;
    --panel:#1b2026;
    --white:#ffffff;
  }
  *{box-sizing:border-box;margin:0;padding:0}
  html,body{width:893px;height:1200px;overflow:hidden;background:var(--white)}
  .flyer{position:relative;width:893px;height:1200px;overflow:hidden;
    font-family:"Open Sans",Arial,sans-serif;color:var(--ink);
    background:linear-gradient(180deg,var(--white) 0,var(--sky) 160px,var(--white) 420px,var(--white) 1080px,var(--sky) 1140px,var(--sky-deep) 1200px)}
  .tagline{position:absolute;left:26px;top:18px;font-family:"Lora",Georgia,serif;font-style:italic;font-weight:600;font-size:21px;color:var(--navy);white-space:nowrap}
  .call-bar{position:absolute;left:0;top:112px;width:560px;height:52px;
    background:linear-gradient(90deg,var(--green-dark),var(--green));
    display:flex;align-items:center;gap:12px;padding-left:26px;color:var(--white);
    font-weight:800;font-size:30px;letter-spacing:.5px;white-space:nowrap}
  .call-bar svg{width:26px;height:26px}
  .brand-panel{position:absolute;left:617px;top:70px;width:262px;height:176px;background:var(--panel);
    display:flex;flex-direction:column;align-items:center;justify-content:center;gap:12px;border:3px solid #444}
  .brand-mark{width:64px;height:64px;border:3px solid var(--gold)}
  .brand-name{font-family:"Open Sans",Arial,sans-serif;font-weight:700;font-size:17px;color:var(--gold);text-align:center;line-height:1.2}
  .seal{position:absolute;left:432px;top:186px;width:92px;height:92px;border-radius:50%;
    background:radial-gradient(circle,#f4f4f4 0,#bfc4c9 70%,#8c949b 100%);box-shadow:0 2px 6px rgba(0,0,0,.3);z-index:2}
  .services{position:absolute;left:26px;top:168px;width:410px}
  .group-title{font-weight:800;font-size:17px;color:var(--teal);margin:14px 0 6px;text-transform:uppercase}
  .group-list{list-style:none}
  .group-list li{position:relative;padding-left:18px;font-size:13.5px;line-height:20.5px;font-weight:600}
  .group-list li::before{content:"";position:absolute;left:0;top:6px;width:9px;height:9px;background:var(--red)}
  .photo{position:absolute;left:440px;width:453px}
  .photo-1{top:262px;height:258px;background:linear-gradient(160deg,#1f4f8c 0,#3f7cc0 40%,#c99a4a 80%,#6b4a22 100%)}
  .photo-2{top:554px;height:214px;background:linear-gradient(180deg,#3e6fa8 0,#8aa9c8 45%,#e9dfc8 70%,#5b5046 100%)}
  .photo-3{top:818px;height:296px;background:linear-gradient(180deg,#5a4530 0,#c8a263 45%,#e9cf95 65%,#3a3a3a 100%)}
  .offer{position:absolute;left:440px;width:453px;text-align:center;font-family:"Roboto Condensed","Arial Narrow",sans-serif;
    font-weight:800;color:var(--red);font-size:18px;line-height:24px;white-space:nowrap;letter-spacing:-.2px}
  .offer-1{top:524px}
  .offer-2{top:780px}
  .offer-3{top:1134px}
  .contact{position:absolute;left:26px;top:1130px;list-style:none}
  .contact li{display:flex;align-items:center;gap:10px;font-size:13.5px;font-weight:600;line-height:22px;color:var(--navy)}
  .contact svg{width:16px;height:16px;fill:var(--navy)}
</style>
</head>
<body>
<div class="flyer">
  <p class="tagline">Reliable on time service, professional and clean</p>

  <div class="call-bar">
    <span>CALL NOW</span>
    <svg viewBox="0 0 24 24" aria-hidden="true"><circle cx="12" cy="12" r="11" fill="none" stroke="#fff" stroke-width="2"/><path d="M8 6l2 0 1 3-1.5 1a7 7 0 0 0 3.5 3.5l1-1.5 3 1v2c0 1-1 2-2 2A9 9 0 0 1 6 8c0-1 1-2 2-2z" fill="#fff"/></svg>
    <span>0400 123 987</span>
  </div>

  <div class="brand-panel">
    <div class="brand-mark"></div>
    <p class="brand-name">Brenna Coltrane Electrical</p>
  </div>

  <div class="seal" role="img" aria-label="Satisfaction guarantee seal"></div>

  <div class="services">
    <h2 class="group-title">Our Business</h2>
    <ul class="group-list">
      <li>Providing high quality professional Electrical service</li>
      <li>With over 31 years combined experience</li>
      <li>Customer service combined with quality work</li>
      <li>Hassle free, honest and reliable</li>
      <li>Delivered on time</li>
      <li>Trained staff ready to assist and work with you to achieve your desired result</li>
    </ul>
    <h2 class="group-title">Our Services</h2>
    <ul class="group-list">
      <li>All Domestic and residential electrical</li>
      <li>Renovations, extensions and re-builds</li>
      <li>Commercial service and construction fit-outs</li>
      <li>Real estate, property maintenance</li>
      <li>Scheduled maintenance</li>
      <li>24/7 Emergency Service</li>
    </ul>
    <h2 class="group-title">Your Business We Can Assist</h2>
    <ul class="group-list">
      <li>Service and Repairs</li>
      <li>Switchboards</li>
      <li>Emergency Lighting</li>
      <li>3 phase power</li>
      <li>Energy Efficiency</li>
      <li>Lighting Installation and Repairs</li>
      <li>Power Circuits</li>
      <li>Electrical Metering</li>
    </ul>
    <h2 class="group-title">Your Home We Can Help</h2>
    <ul class="group-list">
      <li>Downlights</li>
      <li>Ceiling Fans</li>
      <li>Light Replacements</li>
      <li>Switchboard upgrades</li>
      <li>Smoke detector installations</li>
      <li>Power installation or replacement</li>
      <li>Safety switches</li>
      <li>Sensor lights</li>
      <li>Floodlights</li>
      <li>Led replacements</li>
      <li>Exhaust fans</li>
      <li>TV aerial and cable wiring</li>
      <li>Aerial installation</li>
      <li>Data networking and smart wiring</li>
      <li>Internet and telephone</li>
      <li>Intercoms</li>
      <li>Security alarms and cameras</li>
    </ul>
  </div>

  <div class="photo photo-1" role="img" aria-label="Historic city building lit at night"></div>
  <p class="offer offer-1">$95 FREE ELECTRICAL SAFETY CHECK WITH ALL WORK</p>
  <div class="photo photo-2" role="img" aria-label="Modern illuminated house at dusk"></div>
  <p class="offer offer-2">FREE SMOKE DETECTOR TEST AND BATTERY REPLACEMENT</p>
  <div class="photo photo-3" role="img" aria-label="Lit glass entrance of a commercial building"></div>
  <p class="offer offer-3">FREE SAFETY SWITCH CHECK WITH ALL WORK</p>

  <ul class="contact">
    <li><svg viewBox="0 0 24 24" aria-hidden="true"><path d="M12 2a7 7 0 0 0-7 7c0 5 7 13 7 13s7-8 7-13a7 7 0 0 0-7-7zm0 9.5A2.5 2.5 0 1 1 12 6.5a2.5 2.5 0 0 1 0 5z"/></svg>27/88 Harbourview Rd</li>
    <li><svg viewBox="0 0 24 24" aria-hidden="true"><path d="M2 5h20v14H2zM3 6l9 7 9-7" fill="none" stroke="#163a5c" stroke-width="2"/></svg>brenna@coltrane-example.com</li>
    <li><svg viewBox="0 0 24 24" aria-hidden="true"><circle cx="12" cy="12" r="9" fill="none" stroke="#163a5c" stroke-width="2"/><path d="M3 12h18M12 3c3 3 3 15 0 18M12 3c-3 3-3 15 0 18" fill="none" stroke="#163a5c" stroke-width="1.5"/></svg>brennacoltraneelectrical-example.com</li>
  </ul>
</div>
</body>
</html>
```